Brennick Holdings Business Cards

These are professional business cards that are for my family office.
Put fake emails and phone numbers as of now until I finalize those components. This family office controls my families investments, assets, and future. The cards should be professional.
..
.
.
.
I just uploaded another variation of a logo I would like to see as a business card to I am inbeteen which logo to use

Target Market(s)

business

Industry/Entity Type

business

Contact Information for Business Card

Professional, wealth related, finance related.

Requirements
Must have
• Logo

```html
<!DOCTYPE html>
<html lang="en">
<head>
<meta charset="utf-8">
<title>Brennick Holdings Business Cards</title>
<link rel="stylesheet" href="https://fonts.googleapis.com/css2?family=Crimson+Text:wght@400&display=swap">
<style>
  :root {
    --backdrop: #d1d2d4;
    --card-navy: #181e2a;
    --strip-light: #f2f3f5;
    --ink-white: #ffffff;
    --ink-soft: #e9eaec;
  }
  * { margin: 0; padding: 0; box-sizing: border-box; }
  html, body {
    width: 1200px; height: 1000px; overflow: hidden;
    background: var(--backdrop);
    font-family: "Crimson Text", Georgia, serif;
  }
  .canvas { position: relative; width: 1200px; height: 1000px; }

  .card { position: absolute; left: 299px; width: 602px; height: 346px; background: var(--card-navy); overflow: hidden; }
  .card--front { top: 151px; }
  .card--back { top: 520px; }

  .brand-strip { position: absolute; left: 0; top: 0; width: 124px; height: 346px; background: var(--strip-light); }
  .brand-strip__name {
    position: absolute; left: 62px; top: 170px;
    transform: translate(-50%, -50%) rotate(-90deg);
    white-space: nowrap;
    font-size: 38px; line-height: 1; letter-spacing: 0.5px;
    font-variant: small-caps;
    color: var(--card-navy);
  }

  .contact { position: absolute; left: 171px; top: 56px; color: var(--ink-soft); }
  .contact__name { font-size: 24px; letter-spacing: 1.2px; text-transform: uppercase; color: var(--ink-white); line-height: 28px; }
  .contact__title { font-size: 19px; line-height: 24px; }
  .contact__address { margin-top: 21px; font-size: 18px; line-height: 22px; }
  .contact__lines { margin-top: 13px; list-style: none; font-size: 18px; line-height: 24px; }
  .contact__lines li { display: flex; align-items: center; }
  .contact__icon { width: 16px; height: 16px; margin-right: 9px; fill: var(--ink-white); }

  .back-mark {
    position: absolute; left: 219px; top: 66px; width: 164px; height: 164px;
    border: 4px solid var(--ink-white); border-radius: 50%;
  }
  .back-name {
    position: absolute; left: 0; right: 0; top: 240px; text-align: center;
    font-size: 40px; line-height: 1; letter-spacing: 0.5px;
    font-variant: small-caps; color: var(--ink-white);
  }
</style>
</head>
<body>
<main class="canvas">
  <section class="card card--front" aria-label="Business card front">
    <div class="brand-strip">
      <span class="brand-strip__name">Brennick Holdings</span>
    </div>
    <div class="contact">
      <p class="contact__name">Adrian Holloway</p>
      <p class="contact__title">Managing Director</p>
      <p class="contact__address">480 Linden Crest Ave Suite 210,<br>Bayview Shores,<br>90311 California / USA</p>
      <ul class="contact__lines">
        <li>
          <svg class="contact__icon" viewBox="0 0 16 16" aria-hidden="true"><path d="M4 0h8a1.5 1.5 0 0 1 1.5 1.5v13A1.5 1.5 0 0 1 12 16H4a1.5 1.5 0 0 1-1.5-1.5v-13A1.5 1.5 0 0 1 4 0zm.3 2v10h7.4V2zM8 12.8a1 1 0 1 0 0 2 1 1 0 0 0 0-2z"/></svg>
          (555) 214-6XXX
        </li>
        <li>
          <svg class="contact__icon" viewBox="0 0 16 16" aria-hidden="true"><path d="M0 3h16v1.2L8 9 0 4.2zM0 5.8l8 4.8 8-4.8V13H0z"/></svg>
          info@brennickholdings.com
        </li>
        <li>
          <svg class="contact__icon" viewBox="0 0 16 16" aria-hidden="true"><circle cx="8" cy="8" r="7.5"/><path d="M4 4.5c1.5.3 2.5 1.4 2 2.6-.4 1-1.8.9-2 2.3M10 2.5c-.5 1.2.3 2 1.3 2.2M9.5 9.5c1 .2 2 1.2 1.6 2.6" stroke="#181e2a" stroke-width="1.3" fill="none"/></svg>
          www.brennickholdings.com
        </li>
      </ul>
    </div>
  </section>

  <section class="card card--back" aria-label="Business card back">
    <div class="back-mark" aria-hidden="true"></div>
    <p class="back-name">Brennick Holdings</p>
  </section>
</main>
</body>
</html>
```